Wordpress Design Help

We are building a new website for a Data Back Up Company. We have bought a template as below that we are quite happy with but need some help on how to make it a little more punchy.
What we need is some concept on what we can do to make the website look better and more web 2.0, we do not require any coding or templates built. I have an excellent wordpress developer who can do this.
We also need some concepts for the & Day Free Trial Button
I just require high quality images to show the developer what to build.
We also require that the 7 Day Free Trial Image be sent separately (Please see attachment)
As below is the link for the template, also attached are screen shoots of how the website currently looks.
http://demos.lorabrix.com/tamuvo/
Target Market(s)
Small to medium sized business owners who have not reached the size to have thier own IT department yet. We come in and install out software which will do backups to an offsite server automatically for them
Industry/Entity Type
Building
Look and feel
Each slider illustrates characteristics of the customer's brand and the style your logo design should communicate.

```html
<!DOCTYPE html>
<html lang="en">
<head>
<meta charset="utf-8">
<title>Vaultline — Automatic Offsite Backup</title>
<link rel="stylesheet" href="https://fonts.googleapis.com/css2?family=Ubuntu:wght@400;500;700&family=Gelasio:wght@400&family=Oswald:wght@500;700&family=Arimo&display=swap">
<style>
  :root{
    --black:#030303;
    --page:#1b1b1b;
    --green:#4fb84a;
    --green-dark:#1d6b1f;
    --green-deep:#0c4a10;
    --title-green:#166a16;
    --cream-top:#fbfaf3;
    --cream-bottom:#ece8d4;
    --white:#ffffff;
    --text:#1a1a1a;
    --muted:#222;
  }
  *{box-sizing:border-box;margin:0;padding:0}
  html,body{width:1190px;height:1200px;overflow:hidden;background:var(--page)}
  .page{position:absolute;left:0;top:0;width:1002px;height:1011px;transform:scale(1.1876);transform-origin:0 0;
    background:repeating-linear-gradient(45deg,#1e1e1e 0 2px,#151515 2px 4px);font-family:"Ubuntu",sans-serif;color:var(--text)}
  .abs{position:absolute}

  .site-header{left:0;top:0;width:1002px;height:86px;background:var(--black)}
  .brand{left:14px;top:18px;display:flex;align-items:center;gap:12px}
  .brand-mark{width:40px;height:40px;background:var(--green)}
  .brand-name{font:700 34px/1 "Ubuntu",sans-serif;color:var(--white);letter-spacing:1px}
  .call-box{left:714px;top:20px;width:288px;height:46px;background:#111;border:2px solid #2a2a2a;border-right:none;border-radius:4px 0 0 4px;
    font:400 23px/42px "Ubuntu",sans-serif;color:var(--white);padding-left:11px}
  .call-box span{color:var(--green)}

  .main-nav{left:0;top:87px;width:1002px;height:38px;background:linear-gradient(#4a9e45,var(--green-dark) 55%,#0f4f12);border-top:1px solid #6cc466}
  .main-nav ul{list-style:none;display:flex;position:absolute;left:32px;top:4px}
  .main-nav li{font:400 15px/30px "Ubuntu",sans-serif;color:var(--white);padding:0 16px;margin-right:0}
  .main-nav li.current{background:#0c3f10;border:1px solid #2e7d2a;padding:0 15px}
  .search{left:718px;top:6px;width:279px;height:28px;background:var(--white);border:1px solid #ccc;font:400 11px/26px "Ubuntu",sans-serif;color:#888;padding-left:5px}
  .search svg{position:absolute;right:5px;top:5px}

  .intro{left:6px;top:132px;width:990px;height:364px;background:linear-gradient(var(--cream-top),var(--cream-bottom));border:1px solid #d8d3b8}
  .intro h1{position:absolute;left:14px;top:20px;width:325px;font:700 21px/1 "Ubuntu",sans-serif;letter-spacing:.5px;color:var(--black);padding-bottom:9px;border-bottom:1px solid #555}
  .intro p{position:absolute;left:14px;top:62px;width:325px;font:400 10.2px/17px "Ubuntu",sans-serif;text-align:justify;color:var(--muted)}
  .slider{left:361px;top:11px;width:617px;height:345px;background:var(--white);box-shadow:0 1px 4px rgba(0,0,0,.35)}
  .slide-image{position:absolute;left:6px;top:6px;width:605px;height:292px;background:radial-gradient(circle at 62% 45%,#8b8a86 0 14%,#b9b8b4 26%,#cfcfcd 60%,#c4c4c2);}
  .slide-caption{position:absolute;left:9px;top:309px;font:400 17px/1 "Arimo",sans-serif;color:#111}
  .slide-controls{position:absolute;right:10px;top:312px;display:flex;align-items:center;gap:6px;font:700 13px/1 "Arimo",sans-serif;color:#1a4b8a}

  .trial{left:6px;top:503px;width:479px;height:194px;background:linear-gradient(100deg,#08360c,#0d7a1f 45%,#16b43a);border:1px solid #0a4d12}
  .trial-line1{position:absolute;left:9px;top:36px;font:500 34px/1 "Oswald",sans-serif;color:var(--white)}
  .trial-line2{position:absolute;left:9px;top:78px;font:700 54px/1 "Oswald",sans-serif;color:var(--green);letter-spacing:2px}
  .trial-art{position:absolute;left:340px;top:42px;width:126px;height:100px;background:radial-gradient(ellipse at 50% 65%,#e8e8e8 0 40%,#b8b8b8 55%,transparent 70%),radial-gradient(circle at 55% 20%,#5fd03a 0 22%,transparent 24%)}

  .card{background:var(--white);border:1px solid #bbb}
  .card h2{font:400 17.5px/1 "Gelasio",serif;color:var(--title-green);margin:10px 8px 0;padding-bottom:6px;border-bottom:1px dashed #333}
  .card p{font:400 10.5px/17px "Ubuntu",sans-serif;color:#111;margin:7px 10px 0}

  .site-footer{left:0;top:912px;width:1002px;height:42px;background:var(--black);border-top:1px solid #2b2b2b}
  .site-footer small{position:absolute;left:14px;top:16px;font:400 10px/1 "Ubuntu",sans-serif;color:#ddd}
  .social{position:absolute;top:10px;width:22px;height:22px;border-radius:3px}
</style>
</head>
<body>
<div class="page">
  <header class="site-header abs">
    <div class="brand abs"><div class="brand-mark"></div><div class="brand-name">VAULTLINE</div></div>
    <div class="call-box abs">CALL US : <span>888 555 0142</span></div>
  </header>

  <nav class="main-nav abs">
    <ul>
      <li class="current">HOME</li><li>WHAT WE DO</li><li>DOWNLOADS</li><li>GET A QUOTE</li><li>BLOG</li><li>CONTACT US</li>
    </ul>
    <div class="search abs">search this site..
      <svg width="16" height="16" viewBox="0 0 16 16"><circle cx="9.5" cy="6.5" r="4.5" fill="none" stroke="#111" stroke-width="2"/><line x1="6.3" y1="9.7" x2="1.5" y2="14.5" stroke="#111" stroke-width="2.5"/></svg>
    </div>
  </nav>

  <section class="intro abs">
    <h1>WHAT IS VAULTLINE</h1>
    <p>Lorem ipsum dolor sit amet, consectetur adipiscing elit. Nunc laoreet, neque eget pellentesque sodales, metus diam pretium elit, quis lacinia justo nunc vitae odio. Phasellus quis dolor at nisi malesuada iaculis. Maecenas facilisis ultricies enim, non bibendum sapien fermentum eu. Maecenas tellus lacus, bibendum vitae rhoncus ac, porta vestibulum neque. Aenean dignissim elementum magna quis placerat. Aenean nisl dui, euismod vel congue non, pharetra quis lacus. Vestibulum mattis, ante in tempor consequat, risus nisi lobortis nulla, et tristique massa est in arcu. Nam at vehicula magna. Sed eget augue est, quis condimentum felis.</p>
    <div class="slider abs">
      <div class="slide-image" role="img" aria-label="Close-up photograph of an open hard disk drive with its read arm over the platter"></div>
      <div class="slide-caption">Lorem Ipsum Dolor Sit Amet</div>
      <div class="slide-controls">
        <svg width="20" height="12" viewBox="0 0 20 12"><path d="M10 0v12L0 6zM20 0v12L10 6z" fill="#000"/></svg>
        <span>1</span>
        <svg width="12" height="12" viewBox="0 0 12 12"><rect x="1" y="0" width="3.5" height="12" fill="#000"/><rect x="7" y="0" width="3.5" height="12" fill="#000"/></svg>
        <svg width="20" height="12" viewBox="0 0 20 12"><path d="M0 0v12l10-6zM10 0v12l10-6z" fill="#000"/></svg>
      </div>
    </div>
  </section>

  <section class="trial abs">
    <div class="trial-line1">Try Our 7 Day</div>
    <div class="trial-line2">FREE TRIAL</div>
    <div class="trial-art" role="img" aria-label="Illustration of a hard drive with a green download arrow"></div>
  </section>

  <article class="card abs" style="left:495px;top:503px;width:246px;height:194px">
    <h2>Lorem ipsum sit amet dnpo</h2>
    <p>Ut lorem urna, congue ut placerat non, eleifend ut lectus. Sed egestas lorem sit amet lorem faucibus imperdiet. Ut commodo, felis sit amet imperdiet cursus, neque ligula interdum velit, quis eleifend leo lectus nec libero. Vestibulum quis tellus vitae sapien lobortis tristique.Ut commodo</p>
  </article>
  <article class="card abs" style="left:750px;top:503px;width:246px;height:194px">
    <h2>Lorem ipsum sit amet dnpo</h2>
    <p>Ut lorem urna, congue ut placerat non, eleifend ut lectus. Sed egestas lorem sit amet lorem faucibus imperdiet. Ut commodo, felis sit amet imperdiet cursus, neque ligula interdum velit, quis eleifend leo lectus nec libero. Vestibulum quis tellus vitae sapien lobortis tristique.Ut commodo</p>
  </article>

  <article class="card abs" style="left:7px;top:708px;width:322px;height:194px">
    <h2>Lorem ipsum sit amet dnpo</h2>
    <p>Ut lorem urna, congue ut placerat non, eleifend ut lectus. Sed egestas lorem sit amet lorem faucibus imperdiet. Ut commodo, felis sit amet imperdiet cursus, neque ligula interdum velit, quis eleifend leo lectus nec libero. Vestibulum quis tellus vitae sapien lobortis tristique.Ut commodo. Sed egestas lorem sit amet lorem faucibus imperdiet. Ut commodo,felis sit amet imperdiet cursus, neque ligula interdum velit,.</p>
  </article>
  <article class="card abs" style="left:342px;top:708px;width:322px;height:194px">
    <h2>Lorem ipsum sit amet dnpo</h2>
    <p>Ut lorem urna, congue ut placerat non, eleifend ut lectus. Sed egestas lorem sit amet lorem faucibus imperdiet. Ut commodo, felis sit amet imperdiet cursus, neque ligula interdum velit, quis eleifend leo lectus nec libero. Vestibulum quis tellus vitae sapien lobortis tristique.Ut commodo. Sed egestas lorem sit amet lorem faucibus imperdiet. Ut commodo,felis sit amet imperdiet cursus, neque ligula interdum velit,.</p>
  </article>
  <article class="card abs" style="left:676px;top:708px;width:322px;height:194px">
    <h2>Lorem ipsum sit amet dnpo</h2>
    <p>Ut lorem urna, congue ut placerat non, eleifend ut lectus. Sed egestas lorem sit amet lorem faucibus imperdiet. Ut commodo, felis sit amet imperdiet cursus, neque ligula interdum velit, quis eleifend leo lectus nec libero. Vestibulum quis tellus vitae sapien lobortis tristique.Ut commodo. Sed egestas lorem sit amet lorem faucibus imperdiet. Ut commodo,felis sit amet imperdiet cursus, neque ligula interdum velit,.</p>
  </article>

  <footer class="site-footer abs">
    <small>© 2011, vaultline.example</small>
    <span class="social" style="left:920px;background:#3b5a98" aria-label="Social profile"></span>
    <span class="social" style="left:959px;background:#49a9d8" aria-label="Social profile"></span>
  </footer>
</div>
</body>
</html>
```